Willow Brook Meadows - Pelham Ridge Loop

Please use this range of Flyers. Info can be found on our Facebook Page Willow Brook Meadows. W

Colour range- Black with Orange Trim. Logo attached.

Target Market(s)

Horse Owners

Colors
ffcf3e
f78f20
f37122

Requirements
Must have
• Our Logo. Tri-fold
Should not have
• Other photos other than supplied. Do not mix Willow Brook Meadows with Willow Brook Equine Sanctuary. This is only for Willow Brook Meadows.

```html
<!DOCTYPE html>
<html lang="en">
<head>
<meta charset="utf-8">
<title>Willow Brook Meadows – Tri-fold Brochure</title>
<link href="https://fonts.googleapis.com/css2?family=Montserrat:wght@500;600;700&family=Open+Sans:wght@400;600&display=swap" rel="stylesheet">
<style>
  :root {
    --orange: #f37122;
    --amber: #f78f20;
    --gold: #ffcf3e;
    --red: #e24a2e;
    --dark: #3b3a33;
    --ink: #4a4a4a;
    --paper: #ffffff;
    --backdrop: #ececec;
  }
  * { margin: 0; padding: 0; box-sizing: border-box; }
  html, body { width: 669px; height: 1200px; overflow: hidden; }
  body {
    position: relative;
    background: var(--backdrop);
    font-family: "Open Sans", Arial, sans-serif;
    color: var(--ink);
  }
  .spread {
    position: absolute;
    left: 24px;
    width: 620px;
    height: 462px;
    background: var(--paper);
    box-shadow: 0 4px 10px rgba(0,0,0,.22);
    overflow: hidden;
  }
  .spread--outside { top: 112px; }
  .spread--inside { top: 630px; }
  .spread > svg.artwork { position: absolute; inset: 0; }
  .block { position: absolute; }

  .wordmark {
    display: flex; align-items: center; gap: 6px;
    font-family: "Montserrat", Arial, sans-serif;
    font-weight: 600; font-size: 15px; line-height: 1.05;
    color: var(--orange);
  }
  .wordmark__square { width: 22px; height: 22px; background: var(--orange); flex: none; }
  .wordmark--light { color: #fff; }
  .wordmark--light .wordmark__square { background: #fff; }

  .heading {
    font-family: "Montserrat", Arial, sans-serif;
    font-weight: 700; font-size: 10.5px; white-space: nowrap;
    color: var(--red); text-transform: uppercase;
  }
  .heading::after {
    content: ""; display: block; width: 60px; height: 1.5px;
    background: var(--amber); margin-top: 4px;
  }
  .copy { font-size: 7.8px; line-height: 1.4; }
  .copy p + p { margin-top: 6px; }
  .copy .highlight { color: var(--red); font-weight: 600; }

  .community { left: 18px; top: 20px; width: 182px; }
  .community .heading { margin-bottom: 8px; }

  .brand-top { left: 238px; top: 20px; }
  .brand-cover { left: 440px; top: 22px; }

  .contact { left: 226px; top: 300px; width: 170px; text-align: center; color: #fff; }
  .contact__title {
    font-family: "Montserrat", Arial, sans-serif; font-weight: 700; font-size: 13px; letter-spacing: .5px;
  }
  .contact__title::after { content: ""; display: block; width: 40px; height: 1.5px; background: #fff; margin: 5px auto 12px; }
  .contact__item { font-size: 8px; font-weight: 600; margin-bottom: 9px; }
  .contact__item svg { display: block; margin: 0 auto 3px; }

  .cover-title { left: 413px; top: 318px; width: 207px; text-align: center; color: #fff; font-family: "Montserrat", Arial, sans-serif; }
  .cover-title__main { font-weight: 700; font-size: 40px; line-height: 1; letter-spacing: 1px; }
  .cover-title__sub { font-weight: 500; font-size: 14px; letter-spacing: 1.5px; margin-top: 3px; }
  .cover-url { left: 413px; top: 430px; width: 207px; text-align: center; color: #fff; font-size: 8px; font-weight: 600; }

  .news-left { left: 18px; top: 300px; width: 182px; }
  .news-left .heading, .news-mid .heading { margin-bottom: 8px; }
  .news-mid { left: 219px; top: 276px; width: 190px; }
  .url-pill {
    display: inline-block; margin-top: 10px;
    background: var(--red); color: #fff; border-radius: 10px;
    font-size: 7.8px; font-weight: 600; padding: 3px 16px;
  }
  .brand-inside { left: 470px; top: 380px; }
</style>
</head>
<body>

<section class="spread spread--outside" aria-label="Brochure outside">
  <svg class="artwork" viewBox="0 0 620 462" width="620" height="462">
    <defs>
      <linearGradient id="fieldA" x1="0" y1="0" x2="0" y2="1">
        <stop offset="0" stop-color="#8c9a6a"/><stop offset=".55" stop-color="#6f7f45"/><stop offset="1" stop-color="#a38a62"/>
      </linearGradient>
      <linearGradient id="fieldB" x1="0" y1="0" x2="1" y2="1">
        <stop offset="0" stop-color="#9a4a3a"/><stop offset=".5" stop-color="#7d7e6e"/><stop offset="1" stop-color="#5e6a40"/>
      </linearGradient>
      <linearGradient id="fieldC" x1="0" y1="0" x2="0" y2="1">
        <stop offset="0" stop-color="#6e7b4d"/><stop offset="1" stop-color="#b89a6a"/>
      </linearGradient>
    </defs>
    <rect class="panel-dark" x="413" y="0" width="207" height="100" fill="var(--dark)"/>
    <path class="band-red" d="M208,255 C270,300 360,310 430,288 C500,266 560,268 620,262 L620,462 L208,462 Z" fill="var(--red)"/>
    <g role="img" aria-label="Photo: woman leading a grey horse beside a red stable">
      <path d="M413,100 H620 V258 C560,262 490,270 413,300 Z" fill="url(#fieldB)"/>
    </g>
    <path class="trim" d="M413,300 C490,270 560,262 620,258" stroke="var(--amber)" stroke-width="5" fill="none"/>
    <g role="img" aria-label="Photo: rider leading a miniature pony over a wooden obstacle">
      <path d="M0,228 C70,205 150,215 208,262 L208,462 L0,462 Z" fill="url(#fieldA)"/>
    </g>
    <path class="trim" d="M0,212 C75,186 155,198 214,250" stroke="var(--amber)" stroke-width="5" fill="none"/>
    <path class="trim" d="M0,222 C75,196 150,208 208,255" stroke="var(--red)" stroke-width="2" fill="none"/>
    <circle cx="303" cy="196" r="64" fill="none" stroke="var(--red)" stroke-width="3"/>
    <g role="img" aria-label="Photo: saddled buckskin horse on a trail obstacle">
      <circle cx="303" cy="196" r="58" fill="url(#fieldC)" stroke="#fff" stroke-width="5"/>
    </g>
    <line x1="206.5" y1="0" x2="206.5" y2="462" stroke="rgba(0,0,0,.05)"/>
    <line x1="413" y1="0" x2="413" y2="462" stroke="rgba(0,0,0,.05)"/>
  </svg>

  <div class="block community">
    <h2 class="heading">Community</h2>
    <div class="copy">
      <p>Thank you all,<br>We can't thank the rehab team enough (Clara Dunmore, Tessa Marlow, Owen Fitch) for looking after my boy.</p>
      <p>His training stopped due to on-going soreness, which has happened in the past.</p>
      <p>He gets stretched daily and has been sound now 2 years, something has changed.</p>
      <p>Rechecked yesterday, home soon, hopefully a clear diagnosis.</p>
    </div>
  </div>

  <div class="block brand-top wordmark"><span class="wordmark__square"></span><span>Willow Brook<br>Meadows</span></div>
  <div class="block brand-cover wordmark wordmark--light"><span class="wordmark__square"></span><span>Willow Brook<br>Meadows</span></div>

  <div class="block contact">
    <div class="contact__title">CONTACT US</div>
    <div class="contact__item">
      <svg width="12" height="12" viewBox="0 0 12 12"><circle cx="6" cy="6" r="6" fill="#fff"/><path d="M4,3 L5,3 L5.6,4.6 L4.9,5.2 C5.3,6 6,6.7 6.8,7.1 L7.4,6.4 L9,7 L9,8 C9,8.5 8.6,9 8,9 C5.3,8.8 3.2,6.7 3,4 C3,3.4 3.5,3 4,3 Z" fill="var(--red)"/></svg>
      +61 400 555 019
    </div>
    <div class="contact__item">
      <svg width="12" height="12" viewBox="0 0 12 12"><circle cx="6" cy="6" r="6" fill="#fff"/><rect x="3" y="4" width="6" height="4.2" fill="var(--red)"/><path d="M3,4 L6,6.4 L9,4" stroke="#fff" stroke-width=".7" fill="none"/></svg>
      info@willowbrookmeadows.com
    </div>
    <div class="contact__item">
      <svg width="12" height="12" viewBox="0 0 12 12"><circle cx="6" cy="6" r="6" fill="#fff"/><circle cx="6" cy="6" r="3" fill="none" stroke="var(--red)" stroke-width=".8"/><path d="M3,6 H9 M6,3 C4.8,4.6 4.8,7.4 6,9 M6,3 C7.2,4.6 7.2,7.4 6,9" stroke="var(--red)" stroke-width=".6" fill="none"/></svg>
      www.willowbrookmeadows.com
    </div>
  </div>

  <div class="block cover-title">
    <div class="cover-title__main">WILLOW</div>
    <div class="cover-title__sub">BROOK MEADOWS</div>
  </div>
  <div class="block cover-url">www.willowbrookmeadows.com</div>
</section>

<section class="spread spread--inside" aria-label="Brochure inside">
  <svg class="artwork" viewBox="0 0 620 462" width="620" height="462">
    <defs>
      <linearGradient id="fieldD" x1="0" y1="0" x2="0" y2="1">
        <stop offset="0" stop-color="#4a4a3a"/><stop offset=".45" stop-color="#7c8658"/><stop offset="1" stop-color="#5f7a3a"/>
      </linearGradient>
      <linearGradient id="fieldE" x1="0" y1="0" x2="0" y2="1">
        <stop offset="0" stop-color="#b9b2a0"/><stop offset="1" stop-color="#8a8270"/>
      </linearGradient>
      <linearGradient id="fieldF" x1="0" y1="0" x2="0" y2="1">
        <stop offset="0" stop-color="#6f7d4a"/><stop offset="1" stop-color="#c3a677"/>
      </linearGradient>
    </defs>
    <g role="img" aria-label="Photo: handler with a dun horse beside a black fence and coloured poles">
      <path d="M0,0 H620 V150 C560,158 500,198 420,220 C300,252 150,262 0,262 Z" fill="url(#fieldD)"/>
    </g>
    <path class="trim" d="M0,272 C150,272 300,262 420,228 C500,206 560,166 620,160" stroke="var(--amber)" stroke-width="5" fill="none"/>
    <path class="trim" d="M0,280 C150,280 300,270 420,236 C500,214 560,174 620,168" stroke="var(--red)" stroke-width="2" fill="none"/>
    <g role="img" aria-label="Photo: painted wagon sign at the trail entrance">
      <circle cx="354" cy="205" r="55" fill="url(#fieldE)" stroke="#fff" stroke-width="6"/>
    </g>
    <circle cx="514" cy="268" r="86" fill="none" stroke="var(--red)" stroke-width="4"/>
    <g role="img" aria-label="Photo: saddled buckskin horse stepping onto a trail obstacle">
      <circle cx="514" cy="268" r="79" fill="url(#fieldF)" stroke="#fff" stroke-width="5"/>
    </g>
    <line x1="206.5" y1="0" x2="206.5" y2="462" stroke="rgba(0,0,0,.05)"/>
    <line x1="413" y1="0" x2="413" y2="462" stroke="rgba(0,0,0,.05)"/>
  </svg>

  <div class="block news-left">
    <h2 class="heading">Willow Brook Meadows</h2>
    <div class="copy">
      <p>TRAIL OPEN TOMORROW. It's a beautiful day today and tomorrow looks v promising. So the trail will be available.</p>
      <p><span class="highlight">Open from 9.30am to 12.30 pm</span> price is $10 per person. Message for bookings.</p>
      <p>Absolutely beautiful day today and some big and little fun on the trail. Watch out for future dates – subject to weather.</p>
    </div>
  </div>

  <div class="block news-mid">
    <h2 class="heading">Willow Brook Meadows</h2>
    <div class="copy">
      <p>Following on from the success of our launch and subject to some nice May weather we are planning the next Obstacle Days for Wednesday 12th May and Saturday 15th May 2021.</p>
      <p class="highlight">9.30 am until 12.30pm. Session cost is $6.</p>
      <p>If you would like to try the trail but between your own horses we do have ponies available for an additional $25 – lead only.</p>
      <p>PM us for details and bookings.</p>
    </div>
    <span class="url-pill">www.willowbrookmeadows.com</span>
  </div>

  <div class="block brand-inside wordmark"><span class="wordmark__square"></span><span>Willow Brook<br>Meadows</span></div>
</section>

</body>
</html>
```